1 Year Celebration Invitation

A simple, professional flat invitation card for 1 year business anniversary celebration.

The company is a construction company named Stonemark Group. See website: www.stonemark.co.nz

The invitation card must be very elegant but also professional and formal.

the event is being held at Ferndale resort and will be a high end cocktail event.
Updates

Hi Everyone - a small design oversight.

Could we please have the following wording somewhere so we can write in peoples names:

The Management of Stonemark Group would like to invite

___________________________________

to help celebrate its 1 Year Anniversary.

Target Market(s)

company suppliers, customers, staff

Industry/Entity Type

Construction

Requirements
Must have
• Company Logo
One Sided
Event Details:
Time: Friday 27 April 6:30pm for a 7pm start
Location: Torovale Room, Juniper Ferndale Resort, Ferndale Avenue, Ashmoor
Dress: Cocktail
RSVP: info@stonemark.co.nz OR 03 481 2957 by Friday 20th of April
Nice to have
• Ideally 4.00x9.25 Flat Card. But open to other sizes.

```html
<!DOCTYPE html>
<html lang="en">
<head>
<meta charset="utf-8">
<title>Stonemark Group – 1 Year Anniversary Invitation</title>
<link rel="stylesheet" href="https://fonts.googleapis.com/css2?family=Cinzel:wght@400;600;700&display=swap">
<style>
  :root {
    --ink: #3b3032;
    --ink-soft: #4a4042;
    --brand-grey: #6d6668;
    --silver-light: #f4f4f4;
    --silver-mid: #e3e3e3;
    --silver-dark: #d2d2d2;
    --scene-dark: #3a3133;
  }
  html, body {
    margin: 0;
    padding: 0;
    width: 1200px;
    height: 2776px;
    overflow: hidden;
  }
  .invitation {
    position: relative;
    width: 1200px;
    height: 2776px;
    overflow: hidden;
    font-family: "Cinzel", "Times New Roman", serif;
    color: var(--ink);
    background:
      repeating-linear-gradient(180deg,
        rgba(255,255,255,0.35) 0px, rgba(255,255,255,0.35) 1px,
        rgba(0,0,0,0.03) 2px, rgba(0,0,0,0) 4px),
      linear-gradient(180deg, var(--silver-light) 0%, var(--silver-mid) 45%, var(--silver-light) 70%, var(--silver-dark) 100%);
  }
  .line {
    position: absolute;
    left: 0;
    width: 100%;
    margin: 0;
    text-align: center;
    line-height: 1;
    white-space: nowrap;
  }
  .heading-small { font-size: 46px; font-weight: 600; letter-spacing: 2px; }
  .heading-large { font-size: 66px; font-weight: 700; letter-spacing: 2px; }
  .heading-lower { font-size: 42px; font-weight: 600; letter-spacing: 3px; text-transform: lowercase; }
  .heading-large .lead { font-size: 66px; }
  .heading-small .small { font-size: 34px; }
  .numeral { font-size: 64px; }

  .name-line {
    position: absolute;
    left: 167px;
    top: 792px;
    width: 864px;
    height: 3px;
    background: var(--ink);
  }

  .ornament {
    position: absolute;
    left: 273px;
    top: 982px;
    width: 650px;
    height: 150px;
    border-radius: 75px;
    background: radial-gradient(ellipse at center, rgba(59,48,50,0.16) 0%, rgba(59,48,50,0.05) 70%, rgba(59,48,50,0) 100%);
  }

  .detail-label { font-size: 30px; font-weight: 600; letter-spacing: 2px; color: var(--ink-soft); }
  .detail-value { font-size: 44px; font-weight: 700; letter-spacing: 2px; }

  .site-scene {
    position: absolute;
    left: 0;
    top: 2135px;
    width: 1200px;
    height: 641px;
    background: linear-gradient(180deg, rgba(58,49,51,0) 0%, rgba(58,49,51,0.08) 30%, rgba(58,49,51,0.75) 55%, var(--scene-dark) 80%, var(--scene-dark) 100%);
  }

  .brand-name {
    position: absolute;
    left: 520px;
    top: 2300px;
    width: 640px;
    margin: 0;
    text-align: center;
    font-size: 64px;
    font-weight: 700;
    letter-spacing: 1px;
    line-height: 1;
    color: var(--brand-grey);
    white-space: nowrap;
  }
</style>
</head>
<body>
<main class="invitation">
  <p class="line heading-small" style="top:412px;">The <span class="heading-large lead">Management</span> of</p>
  <p class="line heading-large" style="top:490px;">Stonemark Group</p>
  <p class="line heading-lower" style="top:586px;">Would like to invite</p>

  <div class="name-line" aria-hidden="true"></div>

  <p class="line heading-lower" style="top:836px;">To help celebrate its</p>
  <p class="line heading-small" style="top:880px;"><span class="numeral">1</span> Year Anniversary</p>

  <div class="ornament" role="img" aria-label="Decorative scrolled flourish divider"></div>

  <p class="line detail-label" style="top:1286px;">Time:</p>
  <p class="line detail-value" style="top:1326px;">Friday 27 April 6:30pm</p>
  <p class="line detail-value" style="top:1372px;">for a 7pm start</p>

  <p class="line detail-label" style="top:1456px;">Location:</p>
  <p class="line detail-value" style="top:1496px;">Torovale Room, Juniper</p>
  <p class="line detail-value" style="top:1544px;">Ferndale Resort,</p>
  <p class="line detail-value" style="top:1592px;">Ferndale Avenue, Ashmoor</p>

  <p class="line detail-label" style="top:1666px;">Dress:</p>
  <p class="line detail-value" style="top:1702px;">Cocktail</p>

  <p class="line detail-label" style="top:1772px;">RSVP:</p>
  <p class="line detail-value" style="top:1812px;">info@stonemark.co.nz</p>
  <p class="line detail-value" style="top:1858px;">or 03 481 2957</p>
  <p class="line detail-value" style="top:1904px;">by Friday 20th of April</p>

  <div class="site-scene" role="img" aria-label="Silhouette of a city construction site with tower cranes and buildings under construction"></div>

  <p class="brand-name">Stonemark Group</p>
</main>
</body>
</html>
```